Flyer-Design für psychologische Beratungspraxis für Mütter
Zielgruppe
Gelassenheitswerkstatt ist eine psychologische Beratungspraxis. Ich unterstütze Mütter, Schwangere und Frauen mit Kinderwunsch bei Herausforderungen rund um Schwangerschaft, Geburt, Mutterschaft, und damit einhergehenden Problemen.
Aufgabenstellung
Text nochmal geringgradig geändert...siehe Datei anbei

```html
<!DOCTYPE html>
<html lang="de">
<head>
<meta charset="utf-8">
<title>Was also wenn… – Flyer</title>
<link rel="stylesheet" href="https://fonts.googleapis.com/css2?family=League+Spartan:wght@300;400;700&display=swap">
<style>
  :root {
    --accent-blue: #2b2e80;
    --ink: #111111;
    --paper: #ffffff;
  }
  html, body {
    margin: 0;
    padding: 0;
    width: 848px;
    height: 1200px;
    overflow: hidden;
    background: var(--paper);
  }
  .flyer {
    position: relative;
    width: 848px;
    height: 1200px;
    background: var(--paper);
    overflow: hidden;
    font-family: "League Spartan", sans-serif;
    color: var(--ink);
  }
  .corner-band {
    position: absolute;
    top: 0;
    left: 0;
  }
  .headline {
    position: absolute;
    left: 138px;
    top: 190px;
    margin: 0;
    font-weight: 700;
    font-size: 56px;
    line-height: 1;
    letter-spacing: 0.005em;
    white-space: nowrap;
  }
  .body-copy {
    position: absolute;
    left: 138px;
    top: 378px;
    width: 600px;
    margin: 0;
    font-weight: 300;
    font-size: 18.6px;
    line-height: 26.75px;
    letter-spacing: 0.085em;
    white-space: nowrap;
  }
  .body-copy p {
    margin: 0;
  }
  .questions {
    margin-bottom: 26.75px !important;
  }
</style>
</head>
<body>
<main class="flyer">
  <svg class="corner-band" width="848" height="200" viewBox="0 0 848 200" aria-hidden="true">
    <polygon points="0,0 835,0 0,192" fill="var(--accent-blue)"/>
  </svg>

  <h1 class="headline">Was also wenn...</h1>

  <div class="body-copy">
    <p class="questions">
      ...wir gern Mutter wären aber das Leben andere Pläne<br>
      hat?<br>
      ...uns die Erfahrung der Geburt belastet aber niemand<br>
      zuhört, weil ja &nbsp;„jetzt alles ok sei“?<br>
      ...wir unser Kind verloren haben?<br>
      …wir uns treu bleiben wollen aber uns dennoch durch die<br>
      Meinung anderer verunsichern lassen?<br>
      ...wir eben nicht stolz darauf sind, wie wir den letzten<br>
      Schreianfall unseres Babys begleitet haben?<br>
      ...wir weder die Wut unseres Kindes, noch unsere eigene<br>
      Wut gebändigt &nbsp;bekommen?<br>
      ...unser Kind oder wir selbst mit einer Krankheit zu<br>
      kämpfen haben?<br>
      ...wir selbst oder unser Partner uns kaum<br>
      wiedererkennen?<br>
      ...wir mit der Situation überfordert sind, und nicht mehr<br>
      weiter wissen?
    </p>
    <p class="intro">
      Um trotz Rückschlägen ein zufriedenes Leben zu führen<br>
      und um feinfühlig für unsere Kinder da zu sein, benötigen<br>
      wir viel Kraft. Mentale Kraft, die es uns ermöglicht aus<br>
      den Augen unserer Kinder zu sehen, unsere eigenen<br>
      Gefühle zu regulieren und die starken Gefühle unserer<br>
      Kinder auszuhalten und zu begleiten.<br>
      Gemeinsam erarbeiten wir individuelle Strategien, wie<br>
      Sie auf Ihre eigenen Ressourcen besser zugreifen, und<br>
      so mental gestärkt nach vorne schauen können.
    </p>
  </div>
</main>
</body>
</html>
```